Business Card and Letterhead for Vantage Psychology

We need a business card design and letterhead to use for our Psychology firm that specializes in psychoeducational assessments and individual therapy. Our motto is Purpose-Driven Assessments, Meaning-Centered Therapy.Our contact information is as follows:
Vantage Psychology
The Marwick Block - 6127-48St.
Box 2716 Alderwick, AB
T2K 3M8
t 403.555.0148 (VANT)
f 403.555.0172
www.vantagepsychology-example.ca
The business card will be used for two different psychologists so I can supply names nearer to completion. We prefer clean, uncluttered looks.

Target Market(s)

Clients, Educators

Font styles to use
Sans Serif

Colors

Designer to choose colors to be used in the design.

Requirements
Must have
• All relevant contact info, logo, some "white" space.
Nice to have
• It would be nice to see letterhead options that have the logo on the top of the page but also options that have it on the side. I think top of the page is probably our preference.
Should not have
• Too much clutter!

```html
<!DOCTYPE html>
<html lang="en">
<head>
<meta charset="utf-8">
<title>Vantage Psychology – Business Card</title>
<link rel="stylesheet" href="https://fonts.googleapis.com/css2?family=Michroma&family=Poppins:wght@400;500&family=Roboto:wght@400&display=swap">
<style>
  :root {
    --backdrop: #2a2828;
    --paper: #ffffff;
    --brand-blue: #56bcd9;
    --brand-orange: #f9a05c;
    --ink: #4a4a4a;
    --card-shadow: 0 3px 8px rgba(0, 0, 0, 0.55);
  }
  * { box-sizing: border-box; margin: 0; padding: 0; }
  html, body {
    width: 1125px;
    height: 1200px;
    overflow: hidden;
    background: var(--backdrop);
  }
  .sheet { position: relative; width: 1125px; height: 1200px; }
  .card {
    position: absolute;
    left: 171px;
    width: 826px;
    height: 472px;
    box-shadow: var(--card-shadow);
    overflow: hidden;
  }
  .card--front { top: 106px; background: var(--paper); }
  .card--back { top: 639px; background: var(--brand-blue); }

  .holder-name {
    position: absolute;
    left: 44px;
    top: 44px;
    font-family: "Michroma", sans-serif;
    font-weight: 400;
    font-size: 22px;
    letter-spacing: 0.5px;
    color: var(--brand-blue);
  }
  .holder-name__last { color: var(--brand-orange); }
  .holder-role {
    position: absolute;
    left: 44px;
    top: 79px;
    font-family: "Poppins", sans-serif;
    font-size: 18px;
    color: var(--ink);
  }
  .contact {
    position: absolute;
    left: 44px;
    top: 241px;
    font-family: "Poppins", sans-serif;
    font-size: 18px;
    line-height: 23.5px;
    color: var(--ink);
    font-style: normal;
  }
  .contact__address { margin-bottom: 8px; }
  .contact__line { display: block; }
  .contact__line + .contact__line--gap { margin-top: 3px; }

  .brand-front {
    position: absolute;
    left: 478px;
    top: 128px;
    width: 310px;
    display: flex;
    flex-direction: column;
    align-items: center;
    gap: 20px;
  }
  .brand-front__dot {
    width: 160px;
    height: 160px;
    border-radius: 50%;
    background: var(--brand-blue);
  }
  .brand-front__name {
    font-family: "Poppins", sans-serif;
    font-weight: 500;
    font-size: 26px;
    color: var(--brand-blue);
  }

  .brand-back {
    position: absolute;
    left: 0;
    top: 160px;
    width: 100%;
    display: flex;
    flex-direction: column;
    align-items: center;
    gap: 16px;
  }
  .brand-back__dot {
    width: 100px;
    height: 100px;
    border-radius: 50%;
    background: var(--paper);
  }
  .brand-back__name {
    font-family: "Poppins", sans-serif;
    font-weight: 500;
    font-size: 22px;
    color: var(--paper);
  }
  .tagline {
    position: absolute;
    left: 0;
    top: 398px;
    width: 100%;
    text-align: center;
    font-family: "Roboto", sans-serif;
    font-size: 17px;
    color: var(--paper);
  }
</style>
</head>
<body>
<main class="sheet">
  <section class="card card--front" aria-label="Business card front">
    <h1 class="holder-name">DANIEL <span class="holder-name__last">HARTLEY</span></h1>
    <p class="holder-role">President</p>
    <address class="contact">
      <div class="contact__address">
        <span class="contact__line">The Marwick</span>
        <span class="contact__line">Block - 6127-48St.</span>
        <span class="contact__line">Box 2716 Alderwick, AB</span>
        <span class="contact__line">T2K 3M8</span>
      </div>
      <span class="contact__line">P. 403.555.0148 (VANT)</span>
      <span class="contact__line contact__line--gap">F. 403.555.0172</span>
      <span class="contact__line contact__line--gap">www.vantagepsychology-example.ca</span>
    </address>
    <div class="brand-front">
      <span class="brand-front__dot" aria-hidden="true"></span>
      <span class="brand-front__name">Vantage Psychology</span>
    </div>
  </section>

  <section class="card card--back" aria-label="Business card back">
    <div class="brand-back">
      <span class="brand-back__dot" aria-hidden="true"></span>
      <span class="brand-back__name">Vantage Psychology</span>
    </div>
    <p class="tagline">Insight-Led Evaluations | Growth-Focused Counselling.</p>
  </section>
</main>
</body>
</html>
```